Contemporary Business card for Event Manager

Needed for my startup events company in Melbourne. Events I manage will be based within the fashion industry, sporting events, product launches etc. Not weddings or small dinner parties. Therfore I am after something professional and aimed at high end corporate market; but with the added emphasis on not being too conservative or boring. I am happy with a pop of colour e.g. yellow or copper foil.

Target Market(s)

fashion industry, design industry, high end sporting events e.g. Polo, Grand Prix, corporate clients,

Industry/Entity Type

Fashion

Contact Information for Business Card

side 1
Rosa Whitfield (can be upper or lower case, have a feature full stop between first and surname, or at the end of the nameetc) I am open to ideas. I would also be fine with my initials or name as a logo on the front (if this is the case my full name would need to go on the second side of the card.
2nd side:
Mobile: +61 455 718 263
email: rosa.whitfield@kestrelpost.com.au

on one side of the card:
event management | brand activation | Advisory Services

Font styles to use
Serif
Sans Serif

Requirements
Must have
• side 2 must have
• mobile number
• email address
• event management | brand activation | Advisory Services
• ** my full name (Rosa Whitfield) must be on the card somewhere)
Nice to have
• 1st side
• I see the card stock being either a dark grey, light grey, natural white or black (all matt colours on unprocessed card). I see the writing being copper foil, or foil white or foil black.
• To give you a feel for me, think: contemporary, minimalist, I love line drawings, concrete, white with grey vein marble, copper, white, grey, black...yes I do like colour....yellow (but pops of colour) ;) I would like the card to look designer but 'on trend' as I deal with a lot of design and fashion clients....styles - think the sophistication and simplicity of Lisoret or urban contemporary.
• some examples of what I like. Although please don't leet this limit you...I really am happy to have something a little more urban or design focused like a line drawing of an object, person too or a photo image too.
• https://www.pinvaultly.com/pin/837205164932850174/
• https://www.pinvaultly.com/pin/926318450173648205/
• https://www.pinvaultly.com/pin/318604927551203847/
• https://www.pinvaultly.com/pin/50938162477420916/
• https://www.pinvaultly.com/pin/41276039158862793/
• https://www.pinvaultly.com/pin/63098817524506139/
• https://www.pinvaultly.com/pin/704129583366208154/
• https://www.pinvaultly.com/pin/582046317729851460/
• https://www.pinvaultly.com/pin/467318205542097831/
Should not have
• should not look commercial or have cartoonish looking logos. However happy with a simple line drawing or logo with initials etc.

```html
<!DOCTYPE html>
<html lang="en">
<head>
<meta charset="UTF-8">
<title>Rosa Whitfield — Business Card</title>
<link rel="stylesheet" href="https://fonts.googleapis.com/css2?family=Tinos:wght@400&display=swap">
<style>
  :root {
    --page-bg: #ecebe8;
    --card-light: #f4f4f4;
    --card-mid: #dedede;
    --card-dark: #cfcfcf;
    --ink: #111111;
    --card-shadow: rgba(0, 0, 0, 0.18);
  }
  * { box-sizing: border-box; margin: 0; padding: 0; }
  html, body {
    width: 1200px;
    height: 892px;
    overflow: hidden;
    background: var(--page-bg);
  }
  .canvas {
    position: relative;
    width: 1200px;
    height: 892px;
    display: flex;
    flex-direction: column;
    align-items: center;
    justify-content: center;
    gap: 56px;
  }
  .card {
    position: relative;
    width: 600px;
    height: 367px;
    border-radius: 3px;
    overflow: hidden;
    box-shadow: 0 10px 28px var(--card-shadow);
    font-family: "Tinos", "Times New Roman", serif;
    color: var(--ink);
  }
  .card__surface {
    position: absolute;
    inset: 0;
    background: linear-gradient(135deg, var(--card-light) 0%, var(--card-mid) 45%, var(--card-light) 70%, var(--card-dark) 100%);
  }
  .card__content {
    position: absolute;
    inset: 0;
  }
  .card--front .name {
    position: absolute;
    left: 0;
    right: 0;
    top: 138px;
    text-align: center;
    font-size: 64px;
    font-weight: 400;
    letter-spacing: 0.5px;
    line-height: 1;
  }
  .card--back .phone {
    position: absolute;
    left: 176px;
    top: 112px;
    font-size: 36px;
    letter-spacing: 1px;
    line-height: 1;
  }
  .card--back .email {
    position: absolute;
    left: 176px;
    top: 168px;
    font-size: 17px;
    line-height: 1;
  }
  .card--back .services {
    position: absolute;
    left: 150px;
    top: 222px;
    list-style: none;
    font-size: 18px;
    line-height: 1.15;
  }
</style>
</head>
<body>
<main class="canvas">
  <section class="card card--front" aria-label="Business card front">
    <div class="card__surface" role="img" aria-label="Light grey faceted low-poly background"></div>
    <div class="card__content">
      <h1 class="name">Rosa.Whitfield</h1>
    </div>
  </section>

  <section class="card card--back" aria-label="Business card back">
    <div class="card__surface" role="img" aria-label="Light grey faceted low-poly background"></div>
    <div class="card__content">
      <p class="phone">+61 455 718 263</p>
      <p class="email">rosa.whitfield@kestrelpost.com.au</p>
      <ul class="services">
        <li>event management</li>
        <li>brand activation</li>
        <li>Advisory Services</li>
      </ul>
    </div>
  </section>
</main>
</body>
</html>
```